CONTACT US Page and design for website

We need a contact us page for our website. We would like it to have a message area, a map, our information, etc.

Please see the text attachment for what we are looking for. We need to have something that is creative and interesting, modern and professional.

We believe that a contact US page should be very creative because everyone clicks that to contact us. We want it to be super professional, attention grabbing, pleasing to the eye.

PLEASE KEEP THE HEADER AND FOOTER THE SAME, ONLY THE ACTUAL CONTACT US PAGE NEEDS TO BE WORKED ON. THANKS!
We are excited to work with designers for this project.

Target Market(s)

Clients in technology business

Industry/Entity Type

Information Technology

Number of Pages Required

1 page

Font styles to use
Serif

Requirements
Must have
• CHECK THE TEXT ATTACHMENT PLEASE
• Must stay within our design colors and theme.
Nice to have
• see attachment
Should not have
• it should be special

```html
<!DOCTYPE html>
<html lang="en">
<head>
<meta charset="utf-8">
<title>Contact Us – Novarig</title>
<link href="https://fonts.googleapis.com/css2?family=Lato:wght@400;700;900&display=swap" rel="stylesheet">
<style>
:root{
  --teal:#2fbfb4;
  --teal-dark:#1fa79d;
  --ink:#333;
  --muted:#555;
  --rule:#d9d9d9;
  --page:#f4f4f4;
  --footer:#9b9b9b;
  --pill:#b5b5b5;
}
*{margin:0;padding:0;box-sizing:border-box}
html,body{width:836px;height:1200px;overflow:hidden}
body{position:relative;background:#fff;font-family:'Lato',sans-serif;color:var(--ink)}
.abs{position:absolute}

/* header */
.brand{left:120px;top:20px;font-size:26px;font-weight:400;letter-spacing:3px;color:var(--teal)}
.account{left:650px;top:0;width:145px;height:25px;background:var(--pill);border-radius:0 0 22px 22px;display:flex;font-size:8px;color:#444}
.account span{flex:1;display:flex;align-items:center;justify-content:center}
.account span+span{background:#9f9f9f;border-radius:0 0 22px 0;color:#333}
.live-chat{left:606px;top:47px;font-size:10px;color:#444}
.phone-badge{left:669px;top:34px;width:32px;height:32px;border:1px solid var(--rule);border-radius:50%;display:flex;align-items:center;justify-content:center}
.phone-number{left:712px;top:42px;font-size:14px;color:#333}
.nav-rule{left:0;width:836px;height:1px;background:var(--rule)}
.nav{left:43px;top:86px;display:flex;font-size:8.5px;color:#333;letter-spacing:.1px}
.nav a{color:inherit;text-decoration:none;margin-right:20px}
.search{left:650px;top:83px;width:114px;height:25px;border:1px solid #ccc;border-radius:13px;font-size:8.5px;padding:7px 14px;color:#333}
.search svg{position:absolute;right:8px;top:6px}
.cart{left:770px;top:82px;width:28px;height:28px;border:1px solid #ccc;border-radius:50%;display:flex;align-items:center;justify-content:center}
.breadcrumb{left:0;top:114px;width:836px;height:21px;background:var(--teal);font-size:9px;font-weight:900;padding:7px 91px;color:#23484a}
.breadcrumb b{color:#fff;font-weight:900}
.map{left:0;top:135px;width:836px;height:365px;background:linear-gradient(160deg,#d9dcdc 0%,#bfc4c2 45%,#9aa39c 75%,#b9bdbb 100%)}

/* content */
.content{left:0;top:500px;width:836px;height:568px;background:var(--page)}
.title{left:117px;top:558px;font-size:29px;font-weight:400;letter-spacing:1.5px;color:var(--teal)}
.title-rule{left:117px;top:600px;width:136px;height:2px;background:var(--teal)}
.info{left:117px;width:230px;display:flex}
.info svg{flex:none;margin-right:14px}
.info h3{font-size:9px;font-weight:700;letter-spacing:.6px;color:#333;margin-bottom:5px}
.info p{font-size:8.5px;line-height:16px;letter-spacing:.5px;color:var(--muted)}
.info p.hours{line-height:16.2px;color:#333}

.field-label{left:433px;font-size:12px;font-weight:700;letter-spacing:.5px;color:#3a3a3a}
.field{left:433px;width:257px;background:#fff;border:1px solid #bdbdbd;font-size:11.5px;color:#555;padding:0 10px;display:flex;align-items:center;letter-spacing:.3px}
.field.area{align-items:flex-start;padding-top:8px}
.submit{left:434px;top:936px;width:94px;height:38px;background:var(--teal);border-radius:2px;color:#fff;font-size:13px;font-weight:700;letter-spacing:1px;display:flex;align-items:center;justify-content:center}
.availability{left:0;top:1027px;width:836px;text-align:center;font-size:14px;letter-spacing:.6px;color:#444}
.availability b{color:var(--teal);font-weight:700}

/* footer */
.footer{left:0;top:1068px;width:836px;height:132px;background:var(--footer)}
.social{left:342px;top:1083px;display:flex;gap:11px}
.social span{width:29px;height:29px;border:1px solid #ddd;border-radius:50%}
.footer-rule{left:120px;top:1128px;width:600px;height:1px;background:linear-gradient(90deg,transparent,#c9c9c9,transparent)}
.legal{left:0;top:1138px;width:836px;text-align:center;font-size:10px;line-height:13px;color:#fff}
.chat-tab{left:652px;top:1181px;width:159px;height:19px;background:var(--teal);border:1px solid #fff;border-bottom:0;border-radius:3px 3px 0 0;color:#fff;font-size:10px;font-weight:900;padding:4px 7px;letter-spacing:.3px}
.chat-tab svg{position:absolute;right:7px;top:5px}
</style>
</head>
<body>

<header>
  <div class="abs brand">NOVARIG</div>
  <div class="abs account"><span>SIGN UP</span><span>LOGIN</span></div>
  <div class="abs live-chat">LIVE CHAT</div>
  <div class="abs phone-badge">
    <svg width="13" height="13" viewBox="0 0 24 24"><path fill="#2fbfb4" d="M6.6 10.8a15 15 0 0 0 6.6 6.6l2.2-2.2c.3-.3.7-.4 1-.2 1.1.4 2.3.6 3.6.6.6 0 1 .4 1 1V20c0 .6-.4 1-1 1A17 17 0 0 1 3 4c0-.6.4-1 1-1h3.5c.6 0 1 .4 1 1 0 1.3.2 2.5.6 3.6.1.3 0 .7-.2 1z"/></svg>
  </div>
  <div class="abs phone-number">555-014-2200</div>
  <div class="abs nav-rule" style="top:75px"></div>
  <nav class="abs nav">
    <a>SERVERS</a><a>WORKSTATIONS</a><a>COMPONENTS</a><a>VIRTUAL REALITY</a><a>DRONES</a><a>ABOUT US</a><a>BLOG</a><a>RESOURCES</a><a>CONTACT US</a>
  </nav>
  <div class="abs search">Search
    <svg width="11" height="11" viewBox="0 0 24 24"><circle cx="10" cy="10" r="7" fill="none" stroke="#2fbfb4" stroke-width="3"/><path d="M15 15l6 6" stroke="#2fbfb4" stroke-width="3"/></svg>
  </div>
  <div class="abs cart">
    <svg width="14" height="12" viewBox="0 0 24 20"><path d="M2 7h20l-3 11H5z" fill="none" stroke="#2fbfb4" stroke-width="2.4"/><path d="M7 7l5-5 5 5" fill="none" stroke="#2fbfb4" stroke-width="2.4"/></svg>
  </div>
  <div class="abs nav-rule" style="top:112px"></div>
</header>

<div class="abs breadcrumb"><b>HOME</b> / CONTACT US</div>
<div class="abs map" role="img" aria-label="Aerial map of the office headquarters block with a location pin on the street"></div>

<main class="abs content"></main>
<h1 class="abs title">CONTACT US</h1>
<div class="abs title-rule"></div>

<section class="abs info" style="top:616px">
  <svg width="26" height="24" viewBox="0 0 26 24"><path d="M13 2L1 12h4v10h16V12h4z" fill="#2fbfb4"/><rect x="10" y="14" width="6" height="8" fill="#fff"/></svg>
  <div><h3>OFFICE HEADQUARTERS</h3><p>Novarig Tech, LLC. 418 Halden Ave.<br>Marlow Park, CA 90000</p></div>
</section>
<section class="abs info" style="top:678px">
  <svg width="26" height="24" viewBox="0 0 26 24"><circle cx="10" cy="10" r="9" fill="#2fbfb4"/><path d="M4 17l-2 5 6-3z" fill="#2fbfb4"/><circle cx="19" cy="15" r="6" fill="#2fbfb4" stroke="#f4f4f4" stroke-width="1.5"/><circle cx="17" cy="15" r="1" fill="#fff"/><circle cx="19.5" cy="15" r="1" fill="#fff"/><circle cx="22" cy="15" r="1" fill="#fff"/></svg>
  <div><h3>GENERAL INQUIRIES</h3><p>(555)014-2200<br>info@novarig.example</p></div>
</section>
<section class="abs info" style="top:743px">
  <svg width="26" height="24" viewBox="0 0 26 24"><path d="M4 14v-3a9 9 0 0 1 18 0v3" fill="none" stroke="#2fbfb4" stroke-width="2.2"/><circle cx="13" cy="13" r="6" fill="none" stroke="#2fbfb4" stroke-width="2"/><rect x="2" y="11" width="4" height="7" rx="1.5" fill="#2fbfb4"/><rect x="20" y="11" width="4" height="7" rx="1.5" fill="#2fbfb4"/></svg>
  <div><h3>SALES INQUIRIES</h3><p>(555)014-2200<br>sales@novarig.example</p></div>
</section>
<section class="abs info" style="top:807px">
  <svg width="26" height="24" viewBox="0 0 26 24"><rect x="2" y="2" width="18" height="13" fill="none" stroke="#2fbfb4" stroke-width="2"/><path d="M8 15v4h6" stroke="#2fbfb4" stroke-width="2" fill="none"/><path d="M16 10l6 4-2 1 3 4-2 1-3-4-2 2z" fill="#2fbfb4"/></svg>
  <div><h3>PURCHASING INQUIRIES</h3><p>(555)014-2201<br>purchasing@novarig.example</p></div>
</section>
<section class="abs info" style="top:875px">
  <svg width="26" height="30" viewBox="0 0 26 30"><rect x="3" y="3" width="18" height="16" rx="2" fill="none" stroke="#2fbfb4" stroke-width="2"/><rect x="3" y="3" width="18" height="4" fill="#2fbfb4"/><text x="12" y="17" text-anchor="middle" font-family="Lato,sans-serif" font-weight="900" font-size="9" fill="#2fbfb4">5</text><text x="12" y="28" text-anchor="middle" font-family="Lato,sans-serif" font-weight="900" font-size="6.5" fill="#2fbfb4">DAYS</text></svg>
  <div><p class="hours">MONDAY: 8:00AM- 5:00PM<br>TUESDAY: 8:00AM- 5:00PM<br>WEDNESDAY: 8:00AM- 5:00PM<br>THURSDAY: 8:00AM- 5:00PM<br>FRIDAY: 8:00AM- 5:00PM</p></div>
</section>

<form>
  <label class="abs field-label" style="top:573px">NAME *</label>
  <div class="abs field" style="top:601px;height:35px">NAME</div>
  <label class="abs field-label" style="top:655px">E-MAIL *</label>
  <div class="abs field" style="top:683px;height:34px">E-MAIL</div>
  <label class="abs field-label" style="top:738px">PHONE *</label>
  <div class="abs field" style="top:762px;height:34px">PHONE</div>
  <label class="abs field-label" style="top:820px">QUESTIONS/COMMENTS *</label>
  <div class="abs field area" style="top:843px;height:82px;width:258px">MESSAGE</div>
  <div class="abs submit">SUBMIT</div>
</form>

<p class="abs availability">Our dedicated customer service representatives are available <b>24/7</b> by phone.</p>

<footer class="abs footer"></footer>
<div class="abs social"><span></span><span></span><span></span><span></span></div>
<div class="abs footer-rule"></div>
<div class="abs legal">Novarig Tech, LLC.<br>Copyright © 2017</div>
<div class="abs chat-tab">CHAT NOW
  <svg width="10" height="7" viewBox="0 0 10 7"><path d="M1 6l4-4 4 4" fill="none" stroke="#fff" stroke-width="1.6"/></svg>
</div>

</body>
</html>
```